brightpathPRESS is publishing a new book and needs some exceptional cover and layout design!

We are publishing a narrow niche PDF eBook and need both a great cover AND great magazine style layout.

The eBook is a compilation of interviews with 12 financial experts on a particular topic. So the format is is the same for each interview 'chapter'

We are looking for a good front cover/document design that will make what is a pretty dry topic, exciting, interesting and easy to read. Basically - magazine style layout.

The specs for the front cover are:

Title:

The Hurdles and Openings Before Bookkeepers and Planners In Expanding Their Pension Practice In 2014 -2015

by Tom Pelliwick

published by brightpathPRESS

The client would like a similar cover to the one I have attached for your reference. (book front cover example). By no means be limited by this design suggestion. The only caveat is that shots of all interview subjects are included (except the author). These have been included in the zip file.

The design for the text should be elegant and consistent with the design of the front cover. Please format the text in pages 1 to 15 to demonstrate you've understood the brief.

Attached files.

1) MS word version of draft book pages 1 to 15
2) copy of the cover my client would like to emulate.

reminder - this is destined to be a PDF eBook - so looking for some nice eye catching magazine style layout in the design. Columns would be fine.

Good luck!

Brent Malloy
brightpathPRESS

Target Market(s)

Professional Accountants who are running there own businesses

Industry/Entity Type

Financial

Colors

Designer to choose colors to be used in the design.

Requirements
Must have
• The cover must feature headshots of all the interview subjects. The PDF layout must be optimised for viewing on an iPad

```html
<!DOCTYPE html>
<html lang="en">
<head>
<meta charset="utf-8">
<title>Table of Contents – Brightpath Press</title>
<link rel="stylesheet" href="https://fonts.googleapis.com/css2?family=Open+Sans:wght@400;700&display=swap">
<style>
  :root {
    --brand-blue: #416ab2;
    --title-blue: #3e66b2;
    --row-grey: #f3f3f3;
    --row-blue: #d7e4fb;
    --ink: #222222;
    --paper: #ffffff;
  }
  * { margin: 0; padding: 0; box-sizing: border-box; }
  html, body { width: 848px; height: 1200px; overflow: hidden; background: var(--paper); }
  body { font-family: "Open Sans", sans-serif; color: var(--ink); position: relative; }

  .site-band {
    position: absolute; left: 0; top: 0; width: 848px; height: 90px;
    background: var(--brand-blue);
    display: flex; align-items: center; justify-content: center;
  }
  .site-url { color: #fff; font-size: 17.5px; letter-spacing: 1px; }

  .toc-title {
    position: absolute; left: 59px; top: 160px;
    font-size: 35px; font-weight: 400; color: var(--title-blue); line-height: 1.2;
  }
  .toc-rule {
    position: absolute; left: 63px; top: 204px; width: 722px; height: 1px;
    background: var(--title-blue);
  }

  .toc-list {
    position: absolute; left: 57px; top: 225px; width: 728px; list-style: none;
  }
  .toc-entry {
    height: 47px; display: flex; align-items: center;
    padding: 0 20px 0 21px; font-size: 21px; line-height: 1; background: var(--row-grey);
  }
  .toc-entry:nth-child(even) { background: var(--row-blue); }
  .toc-name { white-space: nowrap; padding-right: 6px; }
  .toc-leader {
    flex: 1; min-width: 0; overflow: hidden; white-space: nowrap;
    font-size: 21px; letter-spacing: -0.5px;
  }
  .toc-leader::after {
    content: "..............................................................................................................................................................";
  }
  .toc-page { white-space: nowrap; padding-left: 1px; }

  .publisher {
    position: absolute; left: 0; width: 848px; top: 1120px;
    text-align: center; font-size: 24px; font-weight: 700; color: var(--title-blue);
  }
</style>
</head>
<body>
  <header class="site-band"><span class="site-url">www.brightpathpress.com.au</span></header>

  <h1 class="toc-title">Table of Contents</h1>
  <div class="toc-rule"></div>

  <ol class="toc-list">
    <li class="toc-entry"><span class="toc-name">Foreword</span><span class="toc-leader"></span><span class="toc-page">7</span></li>
    <li class="toc-entry"><span class="toc-name">Grant Hollis</span><span class="toc-leader"></span><span class="toc-page">9</span></li>
    <li class="toc-entry"><span class="toc-name">Tracey Vandermeer</span><span class="toc-leader"></span><span class="toc-page">16</span></li>
    <li class="toc-entry"><span class="toc-name">Mark Ashcombe</span><span class="toc-leader"></span><span class="toc-page">?</span></li>
    <li class="toc-entry"><span class="toc-name">Aaron Pryce</span><span class="toc-leader"></span><span class="toc-page">?</span></li>
    <li class="toc-entry"><span class="toc-name">Peter Galloway</span><span class="toc-leader"></span><span class="toc-page">?</span></li>
    <li class="toc-entry"><span class="toc-name">Jo Fairbrook</span><span class="toc-leader"></span><span class="toc-page">?</span></li>
    <li class="toc-entry"><span class="toc-name">George Kalidis</span><span class="toc-leader"></span><span class="toc-page">?</span></li>
    <li class="toc-entry"><span class="toc-name">Craig Tennant</span><span class="toc-leader"></span><span class="toc-page">?</span></li>
    <li class="toc-entry"><span class="toc-name">Shane Corwin</span><span class="toc-leader"></span><span class="toc-page">?</span></li>
    <li class="toc-entry"><span class="toc-name">Craig Dunmore</span><span class="toc-leader"></span><span class="toc-page">?</span></li>
    <li class="toc-entry"><span class="toc-name">Brent Malloy</span><span class="toc-leader"></span><span class="toc-page">?</span></li>
    <li class="toc-entry"><span class="toc-name">Karnig Avedian</span><span class="toc-leader"></span><span class="toc-page">?</span></li>
    <li class="toc-entry"><span class="toc-name">Ivan Sorell</span><span class="toc-leader"></span><span class="toc-page">?</span></li>
    <li class="toc-entry"><span class="toc-name">Allen Tharp</span><span class="toc-leader"></span><span class="toc-page">?</span></li>
    <li class="toc-entry"><span class="toc-name">Julie Marsh</span><span class="toc-leader"></span><span class="toc-page">?</span></li>
    <li class="toc-entry"><span class="toc-name">Tom Pelliwick</span><span class="toc-leader"></span><span class="toc-page">?</span></li>
    <li class="toc-entry"><span class="toc-name">About the Author</span><span class="toc-leader"></span><span class="toc-page">?</span></li>
  </ol>

  <footer class="publisher">Published by Brightpath Press</footer>
</body>
</html>
```